"Corporate Site Design of Cloud Application Venture"(Wordpress Design Project)

This task is new corporate site design for start-up.
Our company name is "Brindova."
Brindova is a cloud service for users who want to bring their software and settings on multiple computers.
Current beta service page is http://demo.brindova.net . But, now it is not available.
We suggest sample sites below. But, we don't want to follow there. We need you to focus our logo and our company will serve stable service.
http://www.quorvahub.net/design/624957/wordpress-design-by-pelmarix
http://www.quorvahub.net/design/637866/wordpress-design-by-tk
http://www.quorvahub.net/design/613671
http://www.quorvahub.net/design/555672
http://www.quorvahub.net/design/538594
http://www.quorvahub.net/design/544859
http://www.tavinor.net/portfolio/glimbrek/
http://layoutmarsh.net/item/design-company-site/96308
http://www.yorbitstudio.net/images/corporate-dl-thumb.jpg
http://www.vendorquay.net/product-tp/110085749/web_site_design_company.html
(1)we have already had logo-design and please must use it (attached).
we have attached 2 files.
Essential : brindova.ai
voluntary : brindovaicon.ai
(2)Unfortunately, we have no idea now, so depend on you about color, lay-out and something, but we wish people feel deeply impressive when they get our website.
(3)Only if you want to use phrase of my service, please use “Where there is Brindova, there’s your workspace.” (if the English grammar is not correct, please modify it.)
(4)The final design should look modern and sophisticated.
(5)Must have these contents.
In header.
- logo and Friendlattice page link.(http://www.friendlattice.net/brindova)
In Header Menu.
- Top Page (has several news release)
- "News Release" List and News Release Page
- "About Service"
- "About Us"
- "Contact"
And footter has several links.
ex. News release, about service, about us, contact, hiring and so on.

```html
<!DOCTYPE html>
<html lang="en">
<head>
<meta charset="utf-8">
<title>Brindova — Top News</title>
<link rel="stylesheet" href="https://fonts.googleapis.com/css2?family=Nunito:wght@700&family=Fira+Sans:wght@500;600&family=PT+Sans:wght@400;700&family=Open+Sans:wght@400;600;700&display=swap">
<style>
:root{
  --brand:#1b87c9;
  --navy:#0d4f93;
  --nav-top:#1b8fd2;
  --nav-active:#4db6ea;
  --pale:#d9eef7;
  --ink:#222;
  --body:#666;
  --link:#1a6fb0;
  --fb:#3b5998;
  --footer:#1787bf;
}
*{box-sizing:border-box;margin:0;padding:0}
html,body{width:995px;height:1200px;overflow:hidden;background:#fff}
body{position:relative;font-family:"PT Sans",sans-serif;color:var(--body)}
.abs{position:absolute}
a{color:inherit;text-decoration:none}

.brand-logo{left:50px;top:22px;font-family:"Nunito",sans-serif;font-weight:700;font-size:78px;line-height:100px;color:var(--brand);letter-spacing:-1px}
.share-btn{left:793px;top:76px;width:155px;height:28px;border-radius:4px;background:linear-gradient(#3d5d92,#243f6e);color:#fff;font:700 8px "Open Sans",sans-serif;display:flex;align-items:center;gap:8px;padding-left:10px}
.share-btn i{width:16px;height:16px;background:#fff;opacity:.9;border-radius:2px;display:block}

.hero-wrap{left:43px;top:150px;width:906px;height:350px;background:var(--pale);border-radius:18px 18px 30px 30px;box-shadow:0 14px 20px -10px rgba(0,60,110,.18)}
.main-nav{left:43px;top:150px;width:906px;height:36px;border-radius:18px;background:linear-gradient(var(--nav-top),var(--navy));overflow:hidden}
.main-nav a{position:absolute;top:0;line-height:34px;color:#fff;font:600 13px "Open Sans",sans-serif}
.main-nav .active{left:0;width:95px;height:36px;text-align:center;background:linear-gradient(#8fd6f6,var(--nav-active));color:#fff}
.search{left:815px;top:157px;width:117px;height:21px;border-radius:11px;background:#fff;font:italic 11px "Open Sans",sans-serif;color:#888;padding:3px 10px}
.search svg{position:absolute;right:9px;top:5px}

.hero{left:53px;top:198px;width:887px;height:280px;background:#fff;border-radius:10px}
.hero h1{left:57px;top:48px;font:600 24px "Fira Sans",sans-serif;color:#1769b3;letter-spacing:.3px;white-space:nowrap}
.hero p{left:57px;top:86px;width:500px;font:400 17px/25px "PT Sans",sans-serif;color:#666}
.learn-more{left:57px;top:194px;width:138px;height:36px;border-radius:18px;background:linear-gradient(#f2f2f2,#cfcfcf);box-shadow:0 0 0 2px #8fd3f4,0 2px 4px rgba(0,0,0,.2);font:700 12px "Open Sans",sans-serif;color:#666;text-align:center;line-height:36px}
.hero-art{left:632px;top:36px;width:240px;height:215px}
.slider-dots{left:448px;top:489px;display:flex;gap:6px}
.slider-dots span{width:15px;height:15px;border-radius:50%;background:#222;border:3px solid #bbb;display:block}
.slider-dots .on{background:#1b9ad8}

.card{top:540px;width:285px;height:188px;border-radius:14px 14px 0 0;background:linear-gradient(#d6edf7,#fff)}
.card h2{position:absolute;left:6px;top:8px;width:265px;height:35px;border-radius:18px;background:linear-gradient(#1e7fc7,#0a3f84);color:#fff;font:400 17px/35px "PT Sans",sans-serif;padding-left:36px}
.card .icon{position:absolute;left:22px;top:70px;width:48px;height:48px}
.card p{position:absolute;left:93px;top:64px;width:182px;font:400 13px/23px "Open Sans",sans-serif;color:#555;text-align:justify}
.more{width:48px;height:20px;border-radius:3px;background:linear-gradient(#2a8fd0,#0d5a9e);color:#fff;font:700 8px/20px "Open Sans",sans-serif;text-align:center;box-shadow:0 2px 3px rgba(0,0,0,.25)}
.card .more{position:absolute;top:152px}

.news-label{left:50px;top:744px;font:400 17px "Open Sans",sans-serif;color:#1a7cc0}
.news-title{left:53px;top:775px;font:400 17px "Open Sans",sans-serif;color:var(--ink)}
.news-meta{left:53px;top:802px;font:400 11px "Open Sans",sans-serif;color:#333}
.news-rule{left:53px;top:830px;width:577px;border-top:2px dotted #777}
.news-body{left:53px;top:850px;width:607px;font:400 12.4px/18px "Open Sans",sans-serif;color:#666;text-align:justify}
.news-body p+p{margin-top:7px}

.fan-box{left:692px;top:746px;width:251px;height:252px;border:1px solid #98a8c4;background:#fff}
.fan-box header{height:24px;background:var(--fb);color:#fff;font:700 16px/24px "Open Sans",sans-serif;padding-left:7px}
.fan-page{height:60px;background:#eef1f7;border-bottom:1px solid #c8d0e0;position:relative}
.fan-page .thumb{position:absolute;left:9px;top:9px;width:38px;height:38px;background:linear-gradient(#6b4a8a,#2c1f3d)}
.fan-page b{position:absolute;left:57px;top:9px;font:700 14px "Open Sans",sans-serif;color:var(--fb)}
.fan-page span{position:absolute;left:57px;top:33px;font:400 10px "Open Sans",sans-serif;color:#333}
.fan-page span em{font-style:normal;color:var(--fb)}
.fan-count{position:absolute;left:11px;top:93px;font:400 10px "Open Sans",sans-serif;color:#333}
.fan{position:absolute;width:47px;text-align:center;font:400 9px "Open Sans",sans-serif;color:#666}
.fan i{display:block;width:47px;height:47px;margin-bottom:4px}

.footer-links{left:0;top:1020px;width:995px;height:118px;background:var(--pale)}
.footer-links ul{position:absolute;top:16px;list-style:none;font:400 11px/21px "Open Sans",sans-serif;color:var(--link)}
.footer-links li::before{content:"";display:inline-block;width:4px;height:4px;border-radius:50%;background:var(--link);margin:0 8px 2px -12px;vertical-align:middle}
.newsletter-label{left:570px;top:25px;font:700 15px "PT Sans",sans-serif;color:#333;letter-spacing:.5px}
.newsletter-input{left:680px;top:21px;width:243px;height:30px;background:#fff;border:1px solid #bfd3dd;border-radius:2px;font:400 10px/28px "Open Sans",sans-serif;color:#bbb;padding-left:12px}
.subscribe{left:851px;top:63px;width:72px;height:30px;border-radius:2px;background:linear-gradient(#4d80bf,#1f4d8c);border:1px solid #163a6a;color:#fff;font:400 13px/28px "PT Sans",serif;text-align:center}

.footer-bar{left:0;top:1138px;width:995px;height:62px;background:var(--footer)}
.footer-logo{left:46px;top:15px;width:100px;height:34px;background:#fff;border-radius:4px;font:700 20px/34px "Nunito",sans-serif;color:var(--brand);text-align:center}
.copyright{left:157px;top:23px;font:400 10px "Open Sans",sans-serif;color:#fff}
.social{top:19px;width:25px;height:25px;border-radius:4px;box-shadow:0 2px 3px rgba(0,0,0,.3)}
</style>
</head>
<body>

<div class="abs brand-logo">brindova</div>
<a class="abs share-btn" href="http://www.friendlattice.net/brindova"><i></i>Share this with your friends</a>

<div class="abs hero-wrap"></div>
<nav class="abs main-nav">
  <a class="active" href="#">Top News</a>
  <a style="left:127px" href="#">News Release</a>
  <a style="left:251px" href="#">About Service</a>
  <a style="left:375px" href="#">About Us</a>
  <a style="left:472px" href="#">Contact</a>
</nav>
<div class="abs search">Search
  <svg width="11" height="11" viewBox="0 0 11 11"><circle cx="4.5" cy="4.5" r="3.3" fill="none" stroke="#999" stroke-width="1.5"/><path d="M7 7l3 3" stroke="#999" stroke-width="1.8"/></svg>
</div>

<section class="abs hero">
  <h1 class="abs">Where there is Brindova, there’s your workspace.</h1>
  <p class="abs">Brindova synchronizes selected applications between computers based on our proprietary technology.</p>
  <a class="abs learn-more" href="#">LEARN MORE</a>
  <svg class="abs hero-art" role="img" aria-label="Glossy sync symbol with green and blue circular arrows" viewBox="0 0 240 215">
    <defs><radialGradient id="sync" cx="50%" cy="45%" r="55%"><stop offset="0" stop-color="#1f6f9a"/><stop offset=".6" stop-color="#0f3550"/><stop offset="1" stop-color="#6cc53a"/></radialGradient></defs>
    <ellipse cx="120" cy="108" rx="105" ry="105" fill="url(#sync)"/>
  </svg>
</section>
<div class="abs slider-dots"><span></span><span class="on"></span><span></span><span></span><span></span></div>

<article class="abs card" style="left:47px">
  <h2>Brindova</h2>
  <svg class="icon" viewBox="0 0 48 48"><circle cx="24" cy="24" r="24" fill="#333"/><path d="M14 29a6 6 0 0 1 2-11 9 9 0 0 1 17 1 5 5 0 0 1 1 10z" fill="none" stroke="#fff" stroke-width="2.5"/></svg>
  <p style="text-align:left">You can use your apps which you want on any computers anywhere.</p>
  <a class="more" style="left:202px" href="#">MORE</a>
</article>
<article class="abs card" style="left:358px">
  <h2 style="padding-left:31px">Research And Development</h2>
  <svg class="icon" viewBox="0 0 48 48"><circle cx="24" cy="24" r="24" fill="#333"/><path d="M15 33l10-10m3-8a6 6 0 0 1 6 8l-4-1-1-4z" fill="none" stroke="#fff" stroke-width="4" stroke-linecap="round"/></svg>
  <p>You can use your settings, add-ins and so on which you have been used on any computers anywhere.</p>
  <a class="more" style="left:212px" href="#">MORE</a>
</article>
<article class="abs card" style="left:665px">
  <h2 style="padding-left:31px">Investment</h2>
  <svg class="icon" viewBox="0 0 48 48"><circle cx="24" cy="24" r="24" fill="#333"/><text x="24" y="33" text-anchor="middle" font-family="Open Sans, sans-serif" font-weight="700" font-size="26" fill="#fff">$</text></svg>
  <p style="text-align:left">You can share your apps and settings including add-ins with your friends.</p>
  <a class="more" style="left:211px" href="#">MORE</a>
</article>

<h3 class="abs news-label">Top News</h3>
<h4 class="abs news-title">Duis aute irure dolor in reprehenderit in voluptate velit esse</h4>
<div class="abs news-meta">Date : March 22, 2012 &nbsp;&nbsp;Tag : commodo consequat, quis nostrud</div>
<div class="abs news-rule"></div>
<div class="abs news-body">
  <p>At vero eos et accusamus et iusto odio dignissimos ducimus qui blanditiis praesentium voluptatum deleniti atque corrupti quos dolores et quas molestias excepturi sint occaecati cupiditate non provident, similique sunt in culpa qui officia deserunt mollitia animi, id est laborum et dolorum fuga.</p>
  <p>Et harum quidem rerum facilis est et expedita distinctio. Nam libero tempore, cum soluta nobis est eligendi optio cumque nihil impedit quo minus id quod maxime placeat facere possimus, omnis voluptas assumenda est, omnis dolor repellendus. Temporibus autem quibusdam et aut officiis debitis</p>
</div>
<a class="abs more" style="left:610px;top:973px" href="#">MORE</a>

<aside class="abs fan-box">
  <header>friendlattice</header>
  <div class="fan-page">
    <div class="thumb" role="img" aria-label="Page avatar"></div>
    <b>Pixelmarrow</b>
    <span>You like this. <em>Unlike</em></span>
  </div>
  <div class="fan-count">416 people like Pixelmarrow</div>
  <div class="fan" style="left:9px;top:110px"><i role="img" aria-label="Fan profile picture" style="background:#dcdcdc"></i>Tamsin</div>
  <div class="fan" style="left:62px;top:110px"><i role="img" aria-label="Fan profile picture" style="background:linear-gradient(#1a7fb5,#0b3e63)"></i>Orlie</div>
  <div class="fan" style="left:113px;top:110px"><i role="img" aria-label="Fan profile picture" style="background:linear-gradient(#7a8a50,#3e2a4c)"></i>Venna</div>
  <div class="fan" style="left:166px;top:110px"><i role="img" aria-label="Fan profile picture" style="background:linear-gradient(#9a3030,#2a1a1a)"></i>Kabir</div>
  <div class="fan" style="left:9px;top:179px"><i role="img" aria-label="Fan profile picture" style="background:linear-gradient(#6b5a48,#2b241d)"></i>Kabir</div>
  <div class="fan" style="left:62px;top:179px"><i role="img" aria-label="Fan profile picture" style="background:linear-gradient(#8a2c9c,#201238)"></i>Ysolde</div>
  <div class="fan" style="left:113px;top:179px"><i role="img" aria-label="Fan profile picture" style="background:linear-gradient(#e0c060,#6f5a30)"></i>Corvin</div>
  <div class="fan" style="left:166px;top:179px"><i role="img" aria-label="Fan profile picture" style="background:linear-gradient(#8aa0b0,#5a4a40)"></i>Nell</div>
</aside>

<footer>
  <div class="abs footer-links">
    <ul style="left:74px"><li>Company</li><li>Services</li><li>News release</li><li>Message</li></ul>
    <ul style="left:199px"><li>Corporate philosophy</li><li>Code of conducts</li><li>About us</li><li>Our team</li></ul>
    <ul style="left:371px"><li>Contact us</li><li>Brindova on Friendlattice</li><li>Brindova link</li><li>Privacy Policy</li></ul>
    <div class="abs newsletter-label">Newsletter</div>
    <div class="abs newsletter-input">your email address</div>
    <div class="abs subscribe">Subscribe</div>
  </div>
  <div class="abs footer-bar">
    <div class="abs footer-logo">brindova</div>
    <div class="abs copyright">Copyright © 2011 Brindova Inc. All rights reserved.</div>
    <a class="abs social" style="left:817px;background:#3b5998" aria-label="Friendlattice" href="#"></a>
    <a class="abs social" style="left:851px;background:#3fb7ea" aria-label="Chirplet" href="#"></a>
    <a class="abs social" style="left:885px;background:#1a6fa8" aria-label="Linkhaven" href="#"></a>
    <a class="abs social" style="left:919px;background:#f08a1c" aria-label="Feed" href="#"></a>
  </div>
</footer>

</body>
</html>
```